Sales Process

I need a card/page to hand out to my new clients that gives them an over view of our sales process start to finish. Along with 3 points that set us apart from all other competition.
The attached file is my first attempt with other ideas so give your suggestions.
Check out my website to get an idea of who we are. www.brindlefernyards.com

```html
<!DOCTYPE html>
<html lang="en">
<head>
<meta charset="utf-8">
<title>Brindle Fern Yards – Our Process</title>
<link href="https://fonts.googleapis.com/css2?family=Montserrat:ital,wght@0,400;0,500;0,600;0,700;1,400&display=swap" rel="stylesheet">
<style>
  :root{
    --page:#c9c9c9;
    --card-top:#ffffff;
    --card-bottom:#f7f7f7;
    --panel:#2f2f2f;
    --green:#7cc242;
    --ink:#2d2d2d;
    --ink-soft:#555555;
    --white:#ffffff;
  }
  *{margin:0;padding:0;box-sizing:border-box}
  html,body{width:824px;height:1200px;overflow:hidden}
  body{background:var(--page);font-family:"Montserrat",Arial,sans-serif;position:relative}

  .card{position:absolute;left:20px;top:324px;width:784px;height:552px;
    background:var(--card-bottom);box-shadow:0 4px 10px rgba(0,0,0,.25);overflow:hidden}
  .card__top{position:absolute;left:0;top:0;width:784px;height:279px;background:var(--card-top)}
  .values{position:absolute;left:0;top:0;width:472px;height:277px;background:var(--panel);
    border-bottom-right-radius:95px}

  .value{position:absolute;left:52px;width:410px;color:var(--white)}
  .value__icon{position:absolute;left:0;top:0;width:52px;height:52px;border-radius:50%;
    background:radial-gradient(circle,rgba(124,194,66,.45),rgba(124,194,66,.15))}
  .value__title{position:absolute;left:68px;top:0;font-size:16.5px;font-weight:600;white-space:nowrap}
  .value__text{position:absolute;left:68px;top:21px;font-size:12.4px;line-height:15px;white-space:nowrap;font-weight:400}
  .value--team{top:36px}
  .value--quality{top:112px}
  .value--integrity{top:184px}

  .brand{position:absolute;left:500px;top:105px;width:260px;text-align:center}
  .brand__name{display:flex;align-items:center;justify-content:center;gap:10px;
    font-size:24px;font-weight:600;color:var(--ink);white-space:nowrap}
  .brand__dot{width:16px;height:16px;border-radius:50%;background:var(--green)}
  .brand__tagline{margin-top:28px;font-size:11px;font-style:italic;color:var(--ink-soft);white-space:nowrap}

  .step-num{position:absolute;font-size:34px;font-weight:600;color:var(--green);line-height:1}
  .step{position:absolute;width:130px;margin-left:-65px;text-align:center;line-height:15px}
  .step__title{font-size:14.5px;font-weight:600;color:var(--green)}
  .step__text{font-size:12.5px;color:var(--ink)}
  .icon{position:absolute}
  .icon--art{border-radius:50%;background:radial-gradient(circle,rgba(45,45,45,.22),rgba(45,45,45,.05))}
  .bracket{position:absolute;fill:none;stroke:#9a9a9a;stroke-width:1}
</style>
</head>
<body>
<main class="card">
  <div class="card__top"></div>

  <section class="values">
    <div class="value value--team">
      <div class="value__icon" role="img" aria-label="Line icon of joined hands"></div>
      <h2 class="value__title">Teamwork</h2>
      <p class="value__text">Our desire is to exceed our customer’s expectations<br>by developing honest and trustworthy leaders.</p>
    </div>
    <div class="value value--quality">
      <div class="value__icon" role="img" aria-label="Line icon of a thumbs-up seal"></div>
      <h2 class="value__title">Quality/Professionalism</h2>
      <p class="value__text">We are committed to excellent craftsmanship<br>utilizing the best products.</p>
    </div>
    <div class="value value--integrity">
      <div class="value__icon" role="img" aria-label="Line icon of hands fitting puzzle pieces"></div>
      <h2 class="value__title">Integrity and Service</h2>
      <p class="value__text">To build trust by operating with honesty, integrity &amp;<br>serve with excellence &amp; respect.</p>
    </div>
  </section>

  <div class="brand">
    <div class="brand__name"><span class="brand__dot"></span>Brindle Fern Yards</div>
    <p class="brand__tagline">Creating Exceptional Outdoor Living Spaces</p>
  </div>

  <!-- Process steps -->
  <span class="step-num" style="left:58px;top:310px">01</span>
  <svg class="icon" style="left:108px;top:333px" width="58" height="58" viewBox="0 0 58 58" role="img" aria-label="Phone">
    <g fill="none" stroke="#2d2d2d" stroke-width="2" stroke-linecap="round" stroke-linejoin="round">
      <path d="M12 8l7 9-4 5c3 7 8 12 15 16l5-4 9 7-5 7C27 50 6 30 4 14z"/>
      <path d="M36 17a7 7 0 0 1 7 7M37 10a14 14 0 0 1 13 13M38 3a21 21 0 0 1 19 19"/>
    </g>
  </svg>
  <div class="step" style="left:137px;top:403px"><p class="step__title">Initial Call</p><p class="step__text">Can we help?</p></div>

  <svg class="bracket" style="left:190px;top:365px" width="16" height="92"><polyline points="0,0.5 13,0.5 13,89 15,89"/></svg>

  <div class="step" style="left:268px;top:362px"><p class="step__title">Site Visit</p><p class="step__text">Design, Plan<br>&amp; Dream</p></div>
  <svg class="icon" style="left:239px;top:429px" width="52" height="52" viewBox="0 0 52 52" role="img" aria-label="Map pin over hand">
    <g fill="none" stroke="#2d2d2d" stroke-width="2" stroke-linecap="round" stroke-linejoin="round">
      <path d="M32 32C24 22 22 18 22 13a10 10 0 0 1 20 0c0 5-2 9-10 19z"/>
      <circle cx="32" cy="13" r="4"/>
      <path d="M4 34h8v14H4zM12 36l10-2 10 4h8l8-4-6 8-12 4-8-2"/>
    </g>
  </svg>
  <span class="step-num" style="left:280px;top:493px">02</span>

  <svg class="bracket" style="left:326px;top:365px" width="16" height="92"><polyline points="15,0.5 1,0.5 1,89 0,89"/></svg>

  <span class="step-num" style="left:428px;top:304px">03</span>
  <div class="icon icon--art" style="left:368px;top:330px;width:60px;height:60px" role="img" aria-label="Line icon of a seedling held in a hand"></div>
  <div class="step" style="left:399px;top:403px"><p class="step__title">Design</p><p class="step__text">Proposal</p></div>

  <svg class="bracket" style="left:450px;top:374px" width="16" height="92"><polyline points="0,0.5 13,0.5 13,89 15,89"/></svg>

  <div class="step" style="left:527px;top:362px"><p class="step__title">Installation</p><p class="step__text">Construction</p></div>
  <div class="icon icon--art" style="left:498px;top:415px;width:58px;height:64px" role="img" aria-label="Line icon of a young plant in soil"></div>
  <span class="step-num" style="left:575px;top:493px">04</span>

  <svg class="bracket" style="left:575px;top:365px" width="16" height="92"><polyline points="15,0.5 1,0.5 1,89 0,89"/></svg>

  <svg class="icon" style="left:617px;top:324px" width="62" height="62" viewBox="0 0 62 62" role="img" aria-label="Target with arrow">
    <g fill="none" stroke="#2d2d2d" stroke-width="2.2" stroke-linecap="round" stroke-linejoin="round">
      <circle cx="27" cy="35" r="24"/><circle cx="27" cy="35" r="15"/><circle cx="27" cy="35" r="6"/>
      <path d="M27 35L55 7M48 6l7 1-1 7M52 4l3 3"/>
    </g>
  </svg>
  <span class="step-num" style="left:684px;top:304px">05</span>
  <div class="step" style="left:650px;top:403px"><p class="step__title">Complete</p><p class="step__text">Kick Back &amp;<br>relax a smile<br>on your face</p></div>
</main>
</body>
</html>
```